" A VELMIRA é uma empresa de consultoria de Administraçao Contratual de Obras (destacadamente no segmento de infraestrutura e construçao pesada); Elaboraçao de pleitos/reivindicaçoes ("claim") para reequilíbrio econômico-financeiro de contratos de empreendimentos; Gerenciamento de Projetos; Gestao de Empreendimentos; Fiscalizaçao; Auditoria; Gestao Empresarial; Planejamento e Controle de Obras; Análise de Riscos de Empreendimentos; Orçamentos; Suporte para elaboraçao, análise e gestao de contratos. A sede da VELMIRA fica em Brasília/DF, entretanto a atuaçao ocorre em todo o Brasil conforme demanda dos clientes e localizaçao de suas obras. "

```html
<!DOCTYPE html>
<html lang="pt-BR">
<head>
<meta charset="utf-8">
<title>VELMIRA — Pasta</title>
<link href="https://fonts.googleapis.com/css2?family=Open+Sans:wght@400;600;700;800&display=swap" rel="stylesheet">
<style>
  :root {
    --navy: #174a63;
    --navy-soft: #1d5573;
    --sky: #5fa8d3;
    --paper: #ffffff;
    --board: #e6e7e8;
    --board-light: #f4f4f4;
  }
  * { margin: 0; padding: 0; box-sizing: border-box; }
  html, body { width: 1200px; height: 1200px; overflow: hidden; }
  body {
    font-family: "Open Sans", Arial, sans-serif;
    background: radial-gradient(circle at 50% 45%, var(--board-light) 0%, var(--board) 75%);
    position: relative;
  }
  .folder-art { position: absolute; left: 0; top: 0; width: 1200px; height: 1200px; }
  .panel-texture {
    position: absolute; left: 115px; top: 520px; width: 504px; height: 240px;
    background: linear-gradient(180deg, rgba(29,85,115,0) 0%, rgba(29,85,115,0.55) 50%, rgba(29,85,115,0) 100%);
  }
  .section-tag {
    position: absolute; left: 190px; top: 40px;
    color: #fff; font-weight: 700; font-size: 24px; letter-spacing: 1px;
  }
  .brand-small {
    position: absolute; left: 101px; width: 518px; top: 296px;
    text-align: center; color: #fff; font-weight: 800; font-size: 30px; letter-spacing: 2px;
  }
  .brand-cover {
    position: absolute; left: 619px; width: 485px; top: 602px;
    text-align: center; color: var(--navy); font-weight: 800; font-size: 58px; letter-spacing: 3px;
  }
  .contact-list {
    position: absolute; left: 122px; top: 748px; list-style: none;
    color: #fff; font-size: 11px; line-height: 22px;
  }
  .contact-list li { display: flex; align-items: center; gap: 8px; }
  .contact-icon {
    width: 15px; height: 15px; background: #fff; border-radius: 2px;
    display: flex; align-items: center; justify-content: center; flex: none;
  }
  .contact-spacer { width: 15px; height: 15px; flex: none; }
  .address {
    position: absolute; left: 101px; width: 518px; top: 870px;
    text-align: center; color: #fff; font-size: 10px; line-height: 13px;
  }
  .address strong { font-weight: 600; display: block; }
  .website {
    position: absolute; left: 619px; width: 485px; top: 874px;
    text-align: center; color: var(--navy); font-size: 13px; font-weight: 600; letter-spacing: 4px;
  }
</style>
</head>
<body>
<svg class="folder-art" viewBox="0 0 1200 1200" xmlns="http://www.w3.org/2000/svg">
  <defs>
    <linearGradient id="coverFill" x1="0" y1="0" x2="1" y2="1">
      <stop offset="0" stop-color="#ffffff"/>
      <stop offset="1" stop-color="#ebedee"/>
    </linearGradient>
  </defs>
  <polygon points="0,34 40,34 30,82 0,82" fill="var(--sky)"/>
  <polygon points="46,34 427,34 410,82 36,82" fill="var(--navy)"/>
  <rect x="101" y="247" width="518" height="684" fill="var(--navy)"/>
  <rect x="101" y="247" width="6" height="684" fill="#fff"/>
  <rect x="111" y="247" width="4" height="684" fill="var(--sky)"/>
  <rect x="264" y="918" width="192" height="5" fill="var(--sky)"/>
  <path d="M101,924 L619,924 L619,1128 L101,1128 L101,1055 L72,1045 L72,965 L101,955 Z" fill="var(--paper)"/>
  <path d="M101,924 L619,924 L619,1128 L565,1128 C520,1120 505,1060 445,1022 C385,988 250,978 101,978 Z" fill="var(--navy)"/>
  <rect x="619" y="247" width="485" height="684" fill="url(#coverFill)"/>
  <rect x="619" y="247" width="485" height="684" fill="none" stroke="#dcdfe1" stroke-width="1"/>
  <rect x="650" y="881" width="100" height="3" fill="var(--navy)"/>
  <rect x="750" y="881" width="16" height="3" fill="var(--sky)"/>
  <rect x="972" y="881" width="16" height="3" fill="var(--sky)"/>
  <rect x="988" y="881" width="100" height="3" fill="var(--navy)"/>
  <rect x="650" y="902" width="438" height="4" fill="var(--navy)"/>
</svg>

<div class="panel-texture" role="img" aria-label="Faixa decorativa em tons de azul-petróleo"></div>

<div class="section-tag">PASTA</div>

<div class="brand-small">VELMIRA</div>

<ul class="contact-list">
  <li><span class="contact-icon"><svg width="9" height="9" viewBox="0 0 10 10"><path d="M2,1 L4,1 L4.6,3 L3.5,3.8 C4,5 5,6 6.2,6.5 L7,5.4 L9,6 L9,8 C5,8.5 1.5,5 2,1 Z" fill="var(--navy)"/></svg></span>(61) 3345.2870 | (61) 3345.2871</li>
  <li><span class="contact-icon"><svg width="10" height="8" viewBox="0 0 10 8"><rect x="0.5" y="0.5" width="9" height="7" fill="none" stroke="var(--navy)"/><path d="M0.5,0.5 L5,4.5 L9.5,0.5" fill="none" stroke="var(--navy)"/></svg></span>contato@velmira.com.br</li>
  <li><span class="contact-spacer"></span>/velmira</li>
  <li><span class="contact-spacer"></span>@velmira</li>
</ul>

<div class="address">
  <strong>Endereço:</strong>
  Rua das Acácias, 1240 | Centro | Cidade/UF<br>
  Cep: 70000-100
</div>

<div class="brand-cover">VELMIRA</div>

<div class="website">www.velmira.com.br</div>
</body>
</html>
```